Larkspur Vale Management

I need a professional website. My current website is larkspurvalemanagement.com and I hate it. It was created with some AI tool very quickly because I needed a site up and running with no advanced notice. I’m open to all designs .. I trust you, the professionals will deliver the results I’m anxiously awaiting! :)

```html
<!DOCTYPE html>
<html lang="en">
<head>
<meta charset="utf-8">
<title>Larkspur Vale Management</title>
<link href="https://fonts.googleapis.com/css2?family=Exo+2:wght@700;800&family=Roboto:wght@400;500;700&display=swap" rel="stylesheet">
<style>
:root{
  --navy:#1f2a50;
  --navy-deep:#18213f;
  --red:#c2182a;
  --ink:#222;
  --muted:#555;
  --white:#fff;
  --paper:#f1f1f3;
  --black:#060606;
}
*{box-sizing:border-box;margin:0;padding:0}
html,body{width:1200px;height:4525px;overflow:hidden}
body{position:relative;font-family:"Roboto",Arial,sans-serif;color:var(--ink);background:var(--white)}
.abs{position:absolute}
.display{font-family:"Exo 2","Arial Black",sans-serif;font-weight:800;color:var(--navy);text-transform:uppercase;letter-spacing:1px}
.btn{position:absolute;background:var(--red);color:var(--white);font:700 14px "Roboto",sans-serif;text-transform:uppercase;display:flex;align-items:center;justify-content:center;letter-spacing:.3px}
.rule{position:absolute;height:3px;width:68px;background:var(--red)}

/* header */
.topbar{left:0;top:0;width:1200px;height:70px;background:var(--navy)}
.brand-box{left:134px;top:0;width:124px;height:132px;background:var(--white);display:flex;align-items:center;justify-content:center;text-align:center;box-shadow:0 2px 6px rgba(0,0,0,.2)}
.brand-box span{font:700 15px/1.15 "Roboto",sans-serif;color:var(--navy);text-transform:uppercase}
.nav{top:27px;font:500 13px "Roboto",sans-serif;color:var(--white);text-transform:uppercase}
.nav-active:after{content:"";position:absolute;left:0;right:0;top:24px;height:3px;background:var(--white)}
.mailbar{left:768px;top:0;width:432px;height:70px;background:var(--red)}
.mail-icon{left:746px;top:17px;width:36px;height:36px;border-radius:50%;background:var(--navy);display:flex;align-items:center;justify-content:center}
.mail-text{left:800px;top:16px;color:var(--white);font-size:13px;line-height:18px}
.mail-text b{font-size:16px;font-weight:700}

/* hero */
.hero-photo{left:0;top:70px;width:1200px;height:790px;background:linear-gradient(100deg,#f0efed 0%,#e3e1dd 40%,#bdb7ae 65%,#4a4540 85%,#2c2a28 100%)}
.hero-bar{left:144px;top:255px;width:5px;height:265px;background:var(--navy)}
.hero-title{left:160px;top:240px;font-size:72px;line-height:76px;color:var(--navy-deep)}
.hero-sub{left:160px;top:414px;font-size:38px;color:var(--navy-deep)}
.hero-arrow{top:623px;width:36px;height:36px;border-radius:50%;border:2px solid var(--navy);background:var(--white);display:flex;align-items:center;justify-content:center}

/* services */
.section-title{left:0;width:1200px;text-align:center}
.section-sub{left:0;width:1200px;text-align:center;font:700 18px "Exo 2",sans-serif;color:var(--ink);text-transform:uppercase;letter-spacing:.5px}
.section-text{left:150px;width:900px;text-align:center;font-size:14.5px;line-height:21px;color:var(--ink)}
.service{top:1450px;width:300px;text-align:center}
.service h3{font:500 19px "Roboto",sans-serif;color:var(--ink);text-transform:uppercase}
.service.featured h3{color:var(--red)}
.service p{margin-top:14px;font-size:13.5px;line-height:19.5px;color:var(--muted);padding:0 14px}
.service .price{margin-top:14px;font:500 23px "Roboto",sans-serif;color:var(--red)}
.svc-arrow{top:1276px}

/* about */
.about-title{left:142px;top:1980px;font-size:46px;color:var(--white)}
.about-sub{left:142px;top:2065px;font:700 19px "Exo 2",sans-serif;color:var(--white);text-transform:uppercase}
.about-text{left:142px;top:2106px;width:444px;color:var(--white);font-size:14.5px;line-height:21.5px;text-align:justify}
.about-text p+p{margin-top:22px}

/* expertise */
.exp-title{left:613px;top:2858px;font-size:46px}
.exp-sub{left:613px;top:2941px;font:700 19px "Exo 2",sans-serif;color:var(--ink);text-transform:uppercase}
.exp-text{left:613px;top:2980px;width:444px;font-size:14.5px;line-height:21.5px;text-align:justify}

/* contact */
.contact-bg{left:0;top:3343px;width:1200px;height:900px;background:radial-gradient(ellipse at 30% 40%,#f8f8f9,#ececef)}
.label{top:3610px;font-size:14.5px;color:var(--ink)}
.label i{font-style:normal;color:var(--red)}
.field{background:var(--white);border:1px solid #aaa}

/* footer */
.footer-brand{left:141px;top:4262px;width:203px;height:200px;display:flex;align-items:center;gap:12px}
.footer-brand .mark{width:20px;height:20px;background:var(--red);flex:none}
.footer-brand span{font:700 24px/1.15 "Roboto",sans-serif;color:var(--white);text-transform:uppercase}
.footer-nav{left:426px;top:4270px;font:400 20px "Roboto",sans-serif;color:var(--white);word-spacing:2px}
.footer-nav .sep{margin:0 26px}
.f-icon{width:40px;height:40px;border-radius:50%;background:var(--navy);border:2px solid var(--red);display:flex;align-items:center;justify-content:center}
.f-text{color:var(--white);font-size:13px;line-height:18px}
.f-text b{font-size:16px}
.copyright{left:426px;top:4430px;color:var(--white);font-size:19px}
</style>
</head>
<body>

<!-- HERO -->
<div class="abs hero-photo" role="img" aria-label="Photo of a hand holding a pen above a small model house on a desk"></div>
<svg class="abs" style="left:0;top:690px" width="1200" height="240" viewBox="0 0 1200 240">
  <defs><linearGradient id="fadeW" x1="0" y1="0" x2="0" y2="1"><stop offset="0" stop-color="#f3f4f7"/><stop offset="1" stop-color="#fff"/></linearGradient></defs>
  <polygon points="0,30 600,170 1200,30 1200,240 0,240" fill="url(#fadeW)"/>
  <polygon points="0,10 600,130 1200,10 1200,30 600,170 0,30" fill="#1f2a50"/>
  <polygon points="0,30 600,170 1200,30 1200,44 600,172 0,44" fill="#fff"/>
</svg>
<div class="abs hero-bar"></div>
<div class="abs display hero-title">A True<br>Partner,</div>
<div class="abs display hero-sub">Not just a vendor.</div>
<div class="btn" style="left:162px;top:474px;width:156px;height:44px">Get Started</div>
<div class="abs hero-arrow" style="left:143px"><svg width="12" height="12" viewBox="0 0 12 12"><path d="M8 1 3 6l5 5" fill="none" stroke="#1f2a50" stroke-width="2"/></svg></div>
<div class="abs hero-arrow" style="left:186px"><svg width="12" height="12" viewBox="0 0 12 12"><path d="m4 1 5 5-5 5" fill="none" stroke="#1f2a50" stroke-width="2"/></svg></div>

<!-- HEADER -->
<div class="abs topbar"></div>
<div class="abs brand-box"><span>Larkspur<br>Vale<br>Management</span></div>
<div class="abs nav nav-active" style="left:369px">Home</div>
<div class="abs nav" style="left:446px">Services</div>
<div class="abs nav" style="left:547px">About</div>
<div class="abs nav" style="left:630px">Contact</div>
<div class="abs mailbar"></div>
<div class="abs mail-icon"><svg width="16" height="12" viewBox="0 0 16 12"><rect x="0" y="0" width="16" height="12" fill="#fff"/><path d="M0 0 8 7 16 0" fill="none" stroke="#1f2a50" stroke-width="1.5"/></svg></div>
<div class="abs mail-text">Mail us Today:<br><b>info@larkspurvalemanagement.com</b></div>

<!-- SERVICES -->
<div class="abs display section-title" style="top:960px;font-size:46px">Our Services</div>
<div class="rule" style="left:566px;top:1023px"></div>
<div class="abs section-sub" style="top:1040px">Strategic Property Management</div>
<div class="abs section-text" style="top:1071px">Our analysis demonstrates that effective property oversight originates from meticulous operational planning, transparent communication channels, and data-driven performance metrics across every asset class.</div>

<svg class="abs svc-arrow" style="left:62px" width="20" height="30" viewBox="0 0 20 30"><path d="M14 5 5 15l9 10" fill="none" stroke="#111" stroke-width="2.5"/></svg>
<svg class="abs svc-arrow" style="left:1118px" width="20" height="30" viewBox="0 0 20 30"><path d="m6 5 9 10-9 10" fill="none" stroke="#111" stroke-width="2.5"/></svg>

<svg class="abs" style="left:140px;top:1140px" width="282" height="300" viewBox="0 0 282 300">
  <polygon points="141,2 280,77 280,223 141,298 2,223 2,77" fill="#1f2a50"/>
  <polygon points="141,12 270,83 270,217 141,288 12,217 12,83" fill="#fff"/>
  <polygon points="141,20 262,88 262,212 141,280 20,212 20,88" fill="#b89776" role="img" aria-label="Photo of hands arranging paper samples and a clay bowl on a wooden table"/>
</svg>
<svg class="abs" style="left:458px;top:1140px" width="282" height="300" viewBox="0 0 282 300">
  <polygon points="141,2 280,77 280,223 141,298 2,223 2,77" fill="#c2182a"/>
  <polygon points="141,12 270,83 270,217 141,288 12,217 12,83" fill="#fff"/>
  <polygon points="141,20 262,88 262,212 141,280 20,212 20,88" fill="#d8c2a8" role="img" aria-label="Photo of a wooden table lamp beside stacked books"/>
</svg>
<svg class="abs" style="left:778px;top:1140px" width="282" height="300" viewBox="0 0 282 300">
  <polygon points="141,2 280,77 280,223 141,298 2,223 2,77" fill="#1f2a50"/>
  <polygon points="141,12 270,83 270,217 141,288 12,217 12,83" fill="#fff"/>
  <polygon points="141,20 262,88 262,212 141,280 20,212 20,88" fill="#8a7866" role="img" aria-label="Photo of a mushroom lamp and a vase with a calla lily on a side table"/>
</svg>

<div class="abs service" style="left:131px"><h3>Basic Service</h3><p>Describe important details like price, value, length of service, and why it's unique. Or use these sections to showcase different key values of your products or services.</p><div class="price">$99.00</div></div>
<div class="abs service featured" style="left:450px"><h3>Intermediate Service</h3><p>Describe important details like price, value, length of service, and why it's unique. Or use these sections to showcase different key values of your products or services.</p><div class="price">$149.00</div></div>
<div class="abs service" style="left:768px"><h3>Advanced Service</h3><p>Describe important details like price, value, length of service, and why it's unique. Or use these sections to showcase different key values of your products or services.</p><div class="price">$199.00</div></div>

<!-- ABOUT -->
<svg class="abs" style="left:0;top:1690px" width="1200" height="990" viewBox="0 0 1200 990">
  <defs><linearGradient id="fadeTop" x1="0" y1="0" x2="0" y2="1"><stop offset="0" stop-color="#fff"/><stop offset="1" stop-color="#eceef3"/></linearGradient></defs>
  <rect x="0" y="0" width="1200" height="200" fill="url(#fadeTop)"/>
  <polygon points="0,175 600,35 1200,175 1200,205 600,65 0,205" fill="#c2182a"/>
  <polygon points="0,205 600,65 1200,205 1200,216 600,76 0,216" fill="#fff"/>
  <polygon points="0,216 600,76 1200,216 1200,805 600,945 0,805" fill="#1f2a50"/>
  <polygon points="0,805 600,945 1200,805 1200,815 600,955 0,815" fill="#fff"/>
  <polygon points="0,815 600,955 1200,815 1200,845 600,985 0,845" fill="#c2182a"/>
</svg>
<div class="abs display about-title">About Us</div>
<div class="rule" style="left:142px;top:2043px"></div>
<div class="abs about-sub">Our Property Management Solutions</div>
<div class="abs about-text">
  <p>Our organization delivers comprehensive property management solutions that optimize asset performance and tenant satisfaction. By integrating advanced analytics with proven operational frameworks, our specialists ensure each property achieves sustained value appreciation.</p>
  <p>Drawing on decades of collective expertise, the team facilitates regulatory compliance, cost efficiency, and proactive maintenance. This disciplined approach enables owners to preserve capital, enhance occupancy rates, and demonstrate long-term resilience across diverse market conditions.</p>
</div>
<div class="btn" style="left:142px;top:2360px;width:158px;height:42px">Learn More</div>
<svg class="abs" style="left:630px;top:1953px" width="426" height="472" viewBox="0 0 426 472">
  <polygon points="213,0 426,118 426,354 213,472 0,354 0,118" fill="#fff"/>
  <polygon points="213,16 412,126 412,346 213,456 14,346 14,126" fill="#4f6a45" role="img" aria-label="Aerial photo of a tree-lined suburban neighborhood with a city skyline beyond"/>
</svg>

<!-- EXPERTISE -->
<svg class="abs" style="left:142px;top:2758px" width="428" height="472" viewBox="0 0 428 472">
  <polygon points="214,0 428,118 428,354 214,472 0,354 0,118" fill="#1f2a50"/>
  <polygon points="214,14 414,126 414,346 214,458 14,346 14,126" fill="#fff"/>
  <polygon points="214,24 404,131 404,341 214,448 24,341 24,131" fill="#6d6e72" role="img" aria-label="Photo of a person in a suit reviewing plans beside an architectural building model"/>
</svg>
<div class="abs display exp-title">Expertise</div>
<div class="rule" style="left:613px;top:2920px"></div>
<div class="abs exp-sub">Rooted in Asset Preservation</div>
<div class="abs exp-text">The organization applies rigorously tested frameworks and data-driven methodologies to safeguard property value while elevating tenant experience.</div>
<div class="btn" style="left:613px;top:3066px;width:158px;height:44px">Learn More</div>

<!-- CONTACT -->
<div class="abs contact-bg"></div>
<div class="abs display section-title" style="top:3445px;font-size:46px">Get In Touch</div>
<div class="rule" style="left:566px;top:3508px"></div>
<div class="abs section-sub" style="top:3528px">Request a Tailored Proposal</div>
<div class="abs section-text" style="top:3560px">Submit the form to initiate a consultative assessment and explore solutions aligned with your objectives.</div>
<div class="abs label" style="left:141px">First Name<i>*</i></div>
<div class="abs label" style="left:452px">Last Name<i>*</i></div>
<div class="abs label" style="left:763px">Email<i>*</i></div>
<div class="abs field" style="left:141px;top:3637px;width:294px;height:53px"></div>
<div class="abs field" style="left:452px;top:3637px;width:294px;height:53px"></div>
<div class="abs field" style="left:763px;top:3637px;width:294px;height:53px"></div>
<div class="abs label" style="left:141px;top:3710px">Message<i>*</i></div>
<div class="abs field" style="left:141px;top:3737px;width:916px;height:171px"></div>
<div class="btn" style="left:522px;top:3925px;width:156px;height:44px">Send Now</div>

<!-- FOOTER -->
<svg class="abs" style="left:0;top:4070px" width="1200" height="455" viewBox="0 0 1200 455">
  <polygon points="0,110 600,6 1200,110 1200,138 600,34 0,138" fill="#c2182a"/>
  <polygon points="0,138 600,34 1200,138 1200,152 600,48 0,152" fill="#fff"/>
  <polygon points="0,152 600,48 1200,152 1200,455 0,455" fill="#060606"/>
</svg>
<div class="abs footer-brand"><div class="mark"></div><span>Larkspur<br>Vale<br>Management</span></div>
<div class="abs footer-nav">HOME<span class="sep">/</span>SERVICES<span class="sep">/</span>ABOUT<span class="sep">/</span>CONTACT</div>
<div class="abs f-icon" style="left:426px;top:4338px"><svg width="16" height="16" viewBox="0 0 16 16"><path d="M3 1h3l1.5 4-2 1.2a9 9 0 0 0 4.3 4.3L11 8.5l4 1.5v3c0 1-1 2-2 2A13 13 0 0 1 1 3c0-1 1-2 2-2z" fill="#fff"/></svg></div>
<div class="abs f-text" style="left:478px;top:4340px">Call us Today:<br><b>+1 555 014 2290</b></div>
<div class="abs f-icon" style="left:690px;top:4338px"><svg width="16" height="12" viewBox="0 0 16 12"><rect width="16" height="12" fill="#fff"/><path d="M0 0 8 7 16 0" fill="none" stroke="#1f2a50" stroke-width="1.5"/></svg></div>
<div class="abs f-text" style="left:742px;top:4340px">Mail us Today:<br><b>info@larkspurvalemanagement.com</b></div>
<div class="abs copyright">© Copyrights 2026 | All Rights Reserved</div>

</body>
</html>
```